Business card design Needed for new logo / Construction business, home extensions and new builds

We need a business card design using our new logo files which i will attach to this project :)

We are a small construction business specialising in home extensions, new builds and property development. We are very ambitious and would appreciate professional and elegant designs for our new business card.

Very serious about using the services on BriefNest and recently acquired our new logo from here :)

Please get involved, i will feedback when i can as i am very busy but can respond daily, thanks

Target Market(s)

People that want to build onto their houses, new building developments or adding too their existing property

Industry/Entity Type

Construction

Contact Information for Business Card

Hollin Marsh Construction, Tobias Renwick (Managing Director), Tel 07822200444, email - info@hollin-marsh, www.hollin-marsh.co.uk

Colors

Designer to choose colors to be used in the design.

Requirements
Must have
• I like a deep grey on the back please. A lot of you have provided black from and back, try mixing things up a little. The black looks cool 😎 Thanks

```html
<!DOCTYPE html>
<html lang="en">
<head>
<meta charset="utf-8">
<title>Hollin Marsh Construction – Business Cards</title>
<link href="https://fonts.googleapis.com/css2?family=Arimo:wght@400;700&display=swap" rel="stylesheet">
<style>
  :root {
    --stage: #262628;
    --gold-light: #f1cf6a;
    --gold: #d9a532;
    --gold-deep: #b37d1c;
    --ink: #141414;
    --card-grey: #2c2c2e;
    --text-white: #f2f2f2;
    --text-grey: #b9b9bb;
    --accent-gold: #d99a22;
  }
  * { margin: 0; padding: 0; box-sizing: border-box; }
  html, body {
    width: 1200px; height: 779px; overflow: hidden;
    background: var(--stage);
    font-family: "Arimo", Arial, sans-serif;
  }
  .canvas { position: relative; width: 1200px; height: 779px; }
  .card {
    position: absolute; width: 540px; height: 336px;
    box-shadow: 0 14px 30px rgba(0,0,0,.45);
  }
  /* Front */
  .card--front {
    left: 50px; top: 70px;
    background: radial-gradient(ellipse at 50% 42%, var(--gold-light) 0%, var(--gold) 45%, var(--gold-deep) 100%);
    display: flex; flex-direction: column; align-items: center; justify-content: center;
    color: var(--ink);
  }
  .brand { display: flex; flex-direction: column; align-items: center; }
  .brand__mark { width: 34px; height: 34px; margin-bottom: 16px; }
  .brand__name { font-weight: 700; font-size: 26px; letter-spacing: 1.5px; text-transform: uppercase; }
  .brand__sub {
    display: flex; align-items: center; gap: 10px;
    font-weight: 700; font-size: 15px; letter-spacing: 1.5px; text-transform: uppercase; margin-top: 4px;
  }
  .brand__sub::before, .brand__sub::after { content: ""; width: 26px; height: 2px; background: currentColor; }
  .card--front .brand__mark { background: var(--ink); }
  .front__url { margin-top: 34px; font-size: 14px; letter-spacing: 3px; }
  /* Back */
  .card--back {
    left: 610px; top: 373px;
    background: var(--card-grey);
    border-bottom: 2px solid var(--accent-gold);
  }
  .card--back .brand { position: absolute; right: 34px; top: 38px; }
  .card--back .brand__mark { background: var(--accent-gold); width: 28px; height: 28px; margin-bottom: 12px; }
  .card--back .brand__name { font-size: 20px; color: var(--text-white); }
  .card--back .brand__sub { font-size: 12px; color: var(--accent-gold); }
  .card--back .brand__sub::before, .card--back .brand__sub::after { width: 18px; height: 1.5px; }
  .contact { position: absolute; left: 34px; bottom: 34px; }
  .contact__name { color: var(--accent-gold); font-weight: 700; font-size: 24px; }
  .contact__role { color: var(--text-grey); font-size: 15px; margin-top: 2px; }
  .contact__lines { color: var(--text-white); font-size: 14px; margin-top: 20px; white-space: nowrap; }
  .contact__sep { margin: 0 8px; }
</style>
</head>
<body>
<main class="canvas">
  <section class="card card--front" aria-label="Card front">
    <div class="brand">
      <span class="brand__mark"></span>
      <span class="brand__name">Hollin Marsh</span>
      <span class="brand__sub">Construction</span>
    </div>
    <p class="front__url">www.hollin-marsh.co.uk</p>
  </section>

  <section class="card card--back" aria-label="Card back">
    <div class="brand">
      <span class="brand__mark"></span>
      <span class="brand__name">Hollin Marsh</span>
      <span class="brand__sub">Construction</span>
    </div>
    <div class="contact">
      <p class="contact__name">Tobias Renwick</p>
      <p class="contact__role">Managing Director</p>
      <p class="contact__lines">07822200444<span class="contact__sep">|</span>info@hollin-marsh<span class="contact__sep">|</span>www.hollin-marsh.co.uk</p>
    </div>
  </section>
</main>
</body>
</html>
```